Priority Goals poster for school year

We are an elementary school and the past two years have had you help us to design a "poster" that illustrates our goal of the coming year. I am attaching our last year's one, along with some photos of our (ver rough) thinking for next years. The priority goal at top remains the same. Can't wait to see your genius ideas! :)

Target Market(s)

Staff of an elementary school and parents to some (informative) extent as well.

Colors
296eb1
6094c6
fbed22
fbee3f

Requirements
Must have
• items from the white board picture we have attached

```html
<!DOCTYPE html>
<html lang="en">
<head>
<meta charset="utf-8">
<title>Priority Goals 2021-22 – Cedar Ridge Elementary School</title>
<link rel="stylesheet" href="https://fonts.googleapis.com/css2?family=Montserrat:wght@600;800;900&family=Maven+Pro:wght@400;500;700&display=swap">
<style>
  :root {
    --navy: #2b4596;
    --navy-deep: #2a3d96;
    --sky: #72a7d6;
    --gold: #ecc633;
    --gold-ring: #eec81e;
    --white: #ffffff;
    --mist: #eef0f4;
  }
  * { margin: 0; padding: 0; box-sizing: border-box; }
  html, body { width: 848px; height: 1200px; overflow: hidden; background: var(--white); }
  .poster { position: relative; width: 848px; height: 1200px; overflow: hidden; font-family: "Maven Pro", sans-serif; color: var(--navy); }

  .year { position: absolute; top: 8px; left: 0; width: 640px; text-align: center; font-family: "Montserrat", sans-serif; font-weight: 900; font-size: 64px; letter-spacing: 1px; color: var(--navy); line-height: 1; }
  .title-band { position: absolute; top: 77px; left: 0; width: 848px; height: 65px; background: var(--navy); }
  .title { position: absolute; top: 78px; left: 18px; font-family: "Montserrat", sans-serif; font-weight: 800; font-size: 58px; line-height: 62px; color: var(--white); letter-spacing: 1px; }
  .mission-band { position: absolute; top: 142px; left: 0; width: 848px; height: 66px; background: var(--gold); }
  .mission { position: absolute; top: 150px; left: 20px; font-size: 20px; font-weight: 500; line-height: 25px; color: var(--navy); }

  .school-mark { position: absolute; top: 20px; left: 598px; width: 240px; height: 232px; background: var(--white); display: flex; flex-direction: column; justify-content: flex-end; align-items: center; padding-bottom: 14px; }
  .school-mark span { font-family: "Maven Pro", sans-serif; font-weight: 700; color: var(--navy); text-align: center; line-height: 1.05; }
  .school-mark .name { font-size: 34px; }
  .school-mark .sub { font-size: 16.5px; letter-spacing: 0.5px; margin-top: 2px; }

  .backdrop { position: absolute; top: 252px; left: 0; width: 848px; height: 740px; background: linear-gradient(180deg, #f7f7fa 0%, var(--mist) 50%, #f5f5f8 100%); }

  .wheel { position: absolute; top: 0; left: 0; width: 848px; height: 1000px; }
  .wheel text { font-family: "Maven Pro", sans-serif; font-size: 19px; font-weight: 500; }
  .on-dark { fill: var(--white); }
  .on-gold { fill: var(--navy); }
  .strong { font-weight: 700; }

  .promises { position: absolute; top: 994px; left: 0; width: 848px; text-align: center; font-family: "Montserrat", sans-serif; font-weight: 800; font-size: 53px; line-height: 58px; color: var(--navy); }
  .promises-sub { position: absolute; top: 1054px; left: 0; width: 848px; text-align: center; font-family: "Montserrat", sans-serif; font-weight: 600; font-size: 28px; color: var(--navy); }

  .footer-rule { position: absolute; top: 1100px; left: 0; width: 848px; height: 13px; background: var(--gold); }
  .footer { position: absolute; top: 1113px; left: 0; width: 848px; height: 87px; background: var(--navy-deep); color: var(--white); }
  .contact { position: absolute; left: 30px; display: flex; align-items: center; gap: 10px; font-weight: 700; }
  .contact.address { top: 14px; font-size: 19px; }
  .contact.phone { top: 44px; font-size: 29px; }
  .social { position: absolute; top: 24px; left: 582px; display: flex; align-items: center; gap: 9px; font-size: 19px; font-weight: 500; }
  .social-box { width: 32px; height: 32px; background: var(--white); border-radius: 6px; }
</style>
</head>
<body>
<main class="poster">
  <div class="year">2021-22</div>
  <div class="title-band"></div>
  <h1 class="title">PRIORITY GOALS</h1>
  <div class="mission-band"></div>
  <p class="mission">We will accelerate the academic &amp; Social/Emotional<br>Growth of the students we serve by:</p>

  <div class="school-mark">
    <span class="name">CEDAR RIDGE</span>
    <span class="sub">ELEMENTARY SCHOOL</span>
  </div>

  <div class="backdrop" role="img" aria-label="Faint mascot and math sketch backdrop"></div>

  <svg class="wheel" viewBox="0 0 848 1000" aria-label="Goal wheel">
    <circle cx="423" cy="609" r="371" fill="var(--white)" stroke="var(--gold-ring)" stroke-width="9"/>
    <g class="segments">
      <path fill="var(--navy)" d="M423 609 Q331.3 456.4 404.4 254.5 A355 355 0 0 1 660.5 345.2 Q466.1 436.3 423 609Z"/>
      <path fill="var(--gold)" d="M423 609 Q466.1 436.3 660.5 345.2 A355 355 0 0 1 777.5 590.4 Q575.5 517.3 423 609Z"/>
      <path fill="var(--navy)" d="M423 609 Q575.5 517.3 777.5 590.4 A355 355 0 0 1 686.8 846.5 Q595.7 652.1 423 609Z"/>
      <path fill="var(--gold)" d="M423 609 Q595.7 652.1 686.8 846.5 A355 355 0 0 1 441.6 963.5 Q514.7 761.5 423 609Z"/>
      <path fill="var(--sky)" d="M423 609 Q514.7 761.5 441.6 963.5 A355 355 0 0 1 185.5 872.8 Q379.9 781.7 423 609Z"/>
      <path fill="var(--navy)" d="M423 609 Q379.9 781.7 185.5 872.8 A355 355 0 0 1 68.5 627.6 Q270.4 700.7 423 609Z"/>
      <path fill="var(--gold)" d="M423 609 Q270.4 700.7 68.5 627.6 A355 355 0 0 1 159.2 371.5 Q250.3 565.9 423 609Z"/>
      <path fill="var(--sky)" d="M423 609 Q250.3 565.9 159.2 371.5 A355 355 0 0 1 404.4 254.5 Q331.3 456.4 423 609Z"/>
    </g>

    <g class="cap-icon" fill="var(--white)">
      <path d="M350 433 L425 411 L486 431 L423 452 Z"/>
      <path d="M392 440 L392 452 Q423 462 455 452 L455 440 L423 451 Z"/>
      <rect x="470" y="434" width="3" height="16"/>
    </g>

    <path class="heart" fill="var(--white)" stroke="#e1e2e7" stroke-width="7"
      d="M423 738 C360 680 290 620 290 570 C290 530 320 504 355 504 C385 504 410 520 423 536 C436 520 461 504 491 504 C526 504 556 530 556 570 C556 620 486 680 423 738Z"/>

    <g class="classroom-icon" fill="var(--navy)">
      <rect x="319" y="535" width="24" height="18"/>
      <line x1="343" y1="548" x2="356" y2="554" stroke="var(--navy)" stroke-width="2"/>
      <circle cx="361" cy="537" r="4"/>
      <rect x="356" y="543" width="10" height="30" rx="2"/>
      <circle cx="324" cy="570" r="4"/><rect x="317" y="576" width="14" height="8" rx="4"/>
      <circle cx="344" cy="570" r="4"/><rect x="337" y="576" width="14" height="8" rx="4"/>
      <circle cx="365" cy="570" r="4"/><rect x="358" y="576" width="14" height="8" rx="4"/>
    </g>

    <g class="network-icon" fill="var(--navy)">
      <line x1="498" y1="535" x2="480" y2="566" stroke="var(--navy)" stroke-width="3"/>
      <line x1="498" y1="535" x2="516" y2="566" stroke="var(--navy)" stroke-width="3"/>
      <line x1="480" y1="576" x2="516" y2="576" stroke="var(--navy)" stroke-width="3"/>
      <circle cx="498" cy="532" r="6"/><rect x="489" y="540" width="18" height="10" rx="5"/>
      <circle cx="480" cy="564" r="6"/><rect x="471" y="572" width="18" height="10" rx="5"/>
      <circle cx="516" cy="564" r="6"/><rect x="507" y="572" width="18" height="10" rx="5"/>
    </g>

    <g class="school-icon" fill="var(--navy)">
      <rect x="420" y="564" width="2.5" height="28"/>
      <rect x="422" y="564" width="11" height="7"/>
      <rect x="398" y="592" width="48" height="70"/>
      <rect x="372" y="612" width="96" height="50"/>
      <rect x="366" y="664" width="107" height="6"/>
      <circle cx="422" cy="606" r="7" fill="var(--white)"/>
      <circle cx="422" cy="606" r="4"/>
      <g fill="var(--white)">
        <rect x="379" y="622" width="7" height="7"/><rect x="389" y="622" width="7" height="7"/>
        <rect x="379" y="635" width="7" height="7"/><rect x="389" y="635" width="7" height="7"/>
        <rect x="448" y="622" width="7" height="7"/><rect x="458" y="622" width="7" height="7"/>
        <rect x="448" y="635" width="7" height="7"/><rect x="458" y="635" width="7" height="7"/>
        <rect x="413" y="640" width="18" height="22"/>
      </g>
    </g>

    <g class="goal-voices">
      <rect x="304" y="348" width="30" height="22" fill="var(--navy)"/>
      <text x="217" y="366" class="on-dark">Voices of <tspan x="306">All</tspan></text>
      <text x="217" y="393" class="on-dark">Who are we?</text>
      <text x="217" y="421" class="on-dark">Where are we</text>
      <text x="217" y="443" class="on-dark">going?</text>
    </g>
    <text x="402" y="351" class="on-dark">Broaden our Lead</text>
    <g class="goal-staff">
      <text x="556" y="450" class="on-gold">Staff doing what</text>
      <text x="556" y="472" class="on-gold">they Love...</text>
      <text x="557" y="504" class="on-gold">Teaching kids for</text>
      <text x="557" y="526" class="on-gold">Proven Growth</text>
    </g>
    <g class="goal-communicate">
      <text x="583" y="589" class="on-dark">Communicate,</text>
      <text x="583" y="612" class="on-dark">Communicate,</text>
      <text x="583" y="636" class="on-dark">Communicate,</text>
      <circle cx="609" cy="658" r="5" fill="var(--white)"/>
      <rect x="619" y="648" width="112" height="22" fill="var(--white)"/>
      <text x="622" y="665" class="on-gold" style="font-size:17px">Expectations</text>
      <circle cx="626" cy="685" r="5" fill="var(--white)"/>
      <text x="638" y="691" class="on-dark" style="font-size:17px">Support</text>
      <circle cx="636" cy="710" r="5" fill="var(--white)"/>
      <text x="648" y="716" class="on-dark" style="font-size:17px">For Clarity</text>
    </g>
    <g class="goal-partnership">
      <text x="483" y="748" class="on-gold strong">Build Value</text>
      <rect x="479" y="752" width="120" height="23" fill="var(--white)"/>
      <text x="483" y="770" class="on-gold strong">Partnership</text>
      <g fill="var(--navy)">
        <circle cx="487" cy="787" r="5"/><circle cx="487" cy="810" r="5"/>
        <circle cx="487" cy="834" r="5"/><circle cx="487" cy="858" r="5"/>
      </g>
      <text x="496" y="793" class="on-gold" style="font-size:17px">Correct</text>
      <text x="496" y="816" class="on-gold" style="font-size:17px">Celebrate</text>
      <text x="496" y="840" class="on-gold" style="font-size:17px">Strong, Predictable</text>
      <text x="496" y="864" class="on-gold" style="font-size:17px">Laugh,Have Fun</text>
    </g>
    <g class="goal-wellness">
      <rect x="298" y="807" width="100" height="22" fill="var(--navy)"/>
      <text x="305" y="824" class="on-dark strong">Wellness</text>
      <text x="272" y="850" class="on-dark" style="font-size:17px">Mental Health for every</text>
      <text x="272" y="872" class="on-dark" style="font-size:17px">person in our school</text>
      <text x="272" y="894" class="on-dark" style="font-size:17px">community</text>
    </g>
    <g class="goal-intentional">
      <text x="126" y="725" class="on-dark">Be intentional with</text>
      <text x="126" y="747" class="on-dark">each action- Focus</text>
    </g>
    <g class="goal-steps">
      <text x="116" y="548" class="on-gold">Small Measured</text>
      <text x="117" y="574" class="on-gold">Step Towards</text>
      <text x="118" y="600" class="on-gold">Larger Goal</text>
    </g>
  </svg>

  <h2 class="promises">FOUNDATIONAL PROMISES</h2>
  <p class="promises-sub">( 4 YEARS STRONG, BETTER EVERYDAY )</p>

  <div class="footer-rule"></div>
  <footer class="footer">
    <div class="contact address">
      <svg width="20" height="26" viewBox="0 0 20 26" aria-hidden="true"><path d="M10 1 C4.5 1 1 5 1 9.5 C1 16 10 25 10 25 C10 25 19 16 19 9.5 C19 5 15.5 1 10 1Z" fill="none" stroke="#fff" stroke-width="2.5"/><circle cx="10" cy="9.5" r="3.5" fill="none" stroke="#fff" stroke-width="2.5"/></svg>
      <span>1180 Birch Hollow Rd., Lakeview, WA 98000</span>
    </div>
    <div class="contact phone">
      <svg width="20" height="24" viewBox="0 0 20 24" aria-hidden="true"><path d="M6 2 L9 7 L6.5 9.5 Q8 15 12 18 L14.5 15.5 L19 19 L16 22.5 Q8 22 3.5 13 Q1 7 3 3.5 Z" fill="#fff"/></svg>
      <span>555-014-2750</span>
    </div>
    <div class="social">
      <span class="social-box"></span>
      <span>@cedarridgelearners</span>
    </div>
  </footer>
</main>
</body>
</html>
```